Veltrano Energy Business Card Design

website: www.veltranoenergy.example
Project: Business Card Design for Veltrano Energy
Name: Dorian Kettle
Title: Founder / Operations Strategist
Visual Identity & Logo:
Logo File: VEL-Logo-FullGradient-Final.png (Attached).
Color Palette: The brand relies on a distinctive Cyan (Blue) to Lime Green gradient.
Background Preference: We want a Dark Mode aesthetic (Deep Matte Black, Charcoal, or Dark Slate) to make the neon gradient of the logo pop. This feels more "tech/industrial" than a standard white card.
Design Aesthetic (The "Ops" Vibe):
Concept: "Grid & Infrastructure." We are a solar rental company, focusing on logistics and access.
Typography: White, bold sans-serif text for contact info. High contrast against the dark background.
Accents: Use the Cyan or Lime Green from the logo for thin divider lines or edge painting.
Avoid: No orange/gold (clashes with logo). No cartoon leaves.
Layout Requirements:
Front: Large, centered logo. Maybe a subtle UV gloss spot varnish over the logo icon.
Back: Name, Title, Contact Info.
Texture: Matte finish cardstock with gloss elements.
sample mock up of information on card: https://brivomarkco-my.filehost.example/:i:/g/personal/dorian_kettle_veltranoenergy_example/AbCdEfGhIjKlMnOpQrStUvWxYz012345678?e=Xy12Ab
Logo: https://brivomarkco.filehost.example/:i:/s/VeltranoEnergy/ZyXwVuTsRqPoNmLkJiHgFeDcBa9876543210?e=Pq34Cd

```html
<!DOCTYPE html>
<html lang="en">
<head>
<meta charset="utf-8">
<title>Veltrano Energy – Business Card Set</title>
<link rel="stylesheet" href="https://fonts.googleapis.com/css2?family=Montserrat:wght@400;500;700&display=swap">
<style>
  :root {
    --backdrop: #2b2b2c;
    --card-black: #1b1b1c;
    --card-black-deep: #141415;
    --white: #ffffff;
    --soft-white: #e6e6e6;
    --cyan: #1ab3cf;
    --edge-cyan: #1591a8;
    --lime: #7ed63a;
    --gloss-top: rgba(255,255,255,0.16);
    --gloss-bottom: rgba(255,255,255,0.03);
  }
  * { box-sizing: border-box; margin: 0; padding: 0; }
  html, body {
    width: 1200px;
    height: 1200px;
    overflow: hidden;
    background: var(--backdrop);
    font-family: "Montserrat", sans-serif;
  }
  .card-set {
    position: relative;
    width: 1200px;
    height: 1200px;
  }
  .card {
    position: absolute;
    width: 500px;
    height: 286px;
    background: linear-gradient(160deg, var(--card-black) 0%, var(--card-black-deep) 100%);
    border-bottom: 7px solid var(--edge-cyan);
    border-radius: 4px;
    overflow: hidden;
    color: var(--white);
  }
  .card--front-gloss { left: 70px;  top: 150px; }
  .card--back-lime   { left: 630px; top: 300px; }
  .card--back-cyan   { left: 70px;  top: 600px; }
  .card--front-plain { left: 630px; top: 750px; }

  /* Front */
  .spot-gloss {
    position: absolute;
    left: 40px;
    top: 30px;
    width: 420px;
    height: 110px;
    border-radius: 18px;
    background: linear-gradient(180deg, var(--gloss-top), var(--gloss-bottom));
    border: 1px solid rgba(255,255,255,0.08);
  }
  .brand-lockup {
    position: absolute;
    inset: 0;
    display: flex;
    flex-direction: column;
    align-items: center;
    justify-content: center;
    gap: 16px;
  }
  .brand-dot {
    width: 58px;
    height: 58px;
    border-radius: 50%;
    background: var(--cyan);
  }
  .brand-name {
    font-weight: 700;
    font-size: 30px;
    line-height: 1.15;
    letter-spacing: 0.04em;
    text-align: center;
    text-transform: uppercase;
    color: var(--white);
  }

  /* Back */
  .contact-block {
    position: absolute;
    left: 44px;
    top: 48px;
    right: 40px;
  }
  .person-name {
    font-weight: 700;
    font-size: 38px;
    letter-spacing: -0.01em;
  }
  .person-title {
    margin-top: 4px;
    font-weight: 500;
    font-size: 18px;
    color: var(--soft-white);
  }
  .divider {
    margin-top: 12px;
    width: 330px;
    height: 3px;
  }
  .divider--lime { background: var(--lime); }
  .divider--cyan { background: var(--cyan); }
  .contact-list {
    list-style: none;
    margin-top: 28px;
    font-weight: 400;
    font-size: 16px;
    line-height: 1.6;
    color: var(--soft-white);
  }
</style>
</head>
<body>
<main class="card-set">

  <section class="card card--front-gloss" aria-label="Card front with gloss varnish">
    <div class="spot-gloss"></div>
    <div class="brand-lockup">
      <span class="brand-dot"></span>
      <p class="brand-name">Veltrano<br>Energy</p>
    </div>
  </section>

  <section class="card card--back-lime" aria-label="Card back, lime accent">
    <div class="contact-block">
      <h2 class="person-name">Dorian Kettle</h2>
      <p class="person-title">Founder / Operations Strategist</p>
      <div class="divider divider--lime"></div>
      <ul class="contact-list">
        <li>www.veltranoenergy.example</li>
        <li>+1 (555) 010-2283</li>
        <li>dorian@veltranoenergy.example</li>
      </ul>
    </div>
  </section>

  <section class="card card--back-cyan" aria-label="Card back, cyan accent">
    <div class="contact-block">
      <h2 class="person-name">Dorian Kettle</h2>
      <p class="person-title">Founder / Operations Strategist</p>
      <div class="divider divider--cyan"></div>
      <ul class="contact-list">
        <li>www.veltranoenergy.example</li>
        <li>+1 (555) 010-2283</li>
        <li>dorian@veltranoenergy.example</li>
      </ul>
    </div>
  </section>

  <section class="card card--front-plain" aria-label="Card front">
    <div class="brand-lockup">
      <span class="brand-dot"></span>
      <p class="brand-name">Veltrano<br>Energy</p>
    </div>
  </section>

</main>
</body>
</html>
```